Real Estate Agency Chatterlane Cover Photo

We need a Chatterlane cover photo created for our Real Estate Business. We also need this cover photo adapted to several other platforms. Please read this brindlo doc for full specifications of the job https://files.brindlo-example.net/sheet/d/8QwerPLm4ZxVb2NnKs7RtYhUe3_gHdjAoFcWsMvBn/view?mode=share

Please also carefully read the Must Haves/Should Not Haves

Please contact me if you have any queries. Looking forward to seeing your designs!

Owen

Industry/Entity Type

Real Estate Agent

Requirements
Must have
• The Taglines 'More Money In Your Pocket' and sub tagline 'With Our Low Flat Fee To Sell Your Home'

It can then also have other elements e.g our logo, contact details and anything else you think will work well.

It must also have great graphic design work which looks custom and very clean/modern
Should not have
• Must not have poor quality stock images or anything tacky regarding money etc

```html
<!DOCTYPE html>
<html lang="en">
<head>
<meta charset="UTF-8">
<title>KORVALE – More Money In Your Pocket</title>
<link rel="stylesheet" href="https://fonts.googleapis.com/css2?family=Arimo:wght@400;700&display=swap">
<style>
  :root {
    --page-bg: #fdfdfd;
    --panel-bg: #020202;
    --accent-red: #ff0012;
    --text-white: #ffffff;
  }
  * { margin: 0; padding: 0; box-sizing: border-box; }
  html, body {
    width: 1200px;
    height: 1000px;
    overflow: hidden;
    background: var(--page-bg);
    font-family: "Arimo", Arial, sans-serif;
  }
  .cover {
    position: absolute;
    left: 82px;
    top: 229px;
    width: 1036px;
    height: 542px;
    background: var(--panel-bg);
    color: var(--text-white);
  }
  .headline {
    position: absolute;
    left: 0;
    right: 0;
    top: 170px;
    text-align: center;
    font-size: 55px;
    font-weight: 700;
    letter-spacing: 0.2px;
  }
  .subline {
    position: absolute;
    left: 0;
    right: 0;
    top: 241px;
    text-align: center;
    font-size: 25px;
    font-weight: 400;
  }
  .call-badge {
    position: absolute;
    left: 454px;
    top: 293px;
    width: 128px;
    height: 27px;
    border-radius: 14px;
    background: var(--accent-red);
    text-align: center;
    font-size: 20px;
    font-weight: 700;
    line-height: 27px;
  }
  .phone-line {
    position: absolute;
    left: 0;
    right: 0;
    top: 332px;
    display: flex;
    justify-content: center;
    align-items: center;
    gap: 12px;
    font-size: 28px;
    font-weight: 400;
  }
  .phone-icon { width: 32px; height: 32px; }
  .brand-name {
    position: absolute;
    left: 0;
    right: 0;
    top: 420px;
    text-align: center;
    font-size: 36px;
    font-weight: 700;
    letter-spacing: 2px;
    color: var(--accent-red);
  }
  .web-band {
    position: absolute;
    left: 0;
    bottom: 0;
    width: 100%;
    height: 41px;
    background: var(--accent-red);
    text-align: center;
    font-size: 25px;
    line-height: 40px;
    font-weight: 400;
  }
</style>
</head>
<body>
  <section class="cover">
    <h1 class="headline">More Money In Your Pocket</h1>
    <p class="subline">With Our Low Flate Fee To Sell Your Home</p>
    <div class="call-badge">CALL NOW</div>
    <div class="phone-line">
      <svg class="phone-icon" viewBox="0 0 32 32" aria-hidden="true">
        <path d="M7 3 L12 3 L14 10 L10.5 12.5 C12.5 17 15 19.5 19.5 21.5 L22 18 L29 20 L29 25 C29 27 27 29 25 29 C14 28 4 18 3 7 C3 5 5 3 7 3 Z"
              fill="none" stroke="#ffffff" stroke-width="2.2" stroke-linejoin="round"/>
        <path d="M18 4 A10 10 0 0 1 28 14" fill="none" stroke="#ffffff" stroke-width="2" stroke-linecap="round"/>
        <path d="M18 8.5 A5.5 5.5 0 0 1 23.5 14" fill="none" stroke="#ffffff" stroke-width="2" stroke-linecap="round"/>
      </svg>
      <span class="phone-number">+612 5081 3947</span>
    </div>
    <div class="brand-name">KORVALE</div>
    <div class="web-band">www.korvale-homes.com</div>
  </section>
</body>
</html>
```